Tree Service Billboard 20x8 ft

We need a billboard design for a tree service company.
The billboard is 20ft x 8 ft so we need a design that is capable to stretching to those dimensions without loosing quality.
I have attached a series of images.
Image 1- Simply a billboard that I think looks good that I would like you to use for inspiration. I am aiming for the same format only no color in the wording, just black white, or gray. I like the the trees in the background, the logo placed to the left, and wording on the right.
Image 2- Current Logo I would like to the left of the billboard
Image 3- Another format of current logo if needed.
Image 4- A drawn out design template
Image 5- Another drawn out design template

Specific things I am looking for
-The contact number to be the largest thing on the design
-The logo on the design
-Key points to the design to say:
Tree Removal
Tree Trimming
Land Development
Stump Grinding
Storm Response
Insured
Free Bids
-The facebook logo
-The Google Logo

```html
<!DOCTYPE html>
<html lang="en">
<head>
<meta charset="utf-8">
<title>Hollis Tree Service Billboard</title>
<link rel="stylesheet" href="https://fonts.googleapis.com/css2?family=Barlow+Condensed:wght@600;700&display=swap">
<style>
  :root {
    --page: #ffffff;
    --forest-deep: #0b0d0a;
    --forest-mid: #1c2417;
    --forest-light: #5a553a;
    --panel: #dcdbdc;
    --panel-edge: #6a6a6a;
    --ink: #111111;
    --name-gray: #6a6a6a;
    --white: #ffffff;
  }
  html, body {
    margin: 0;
    width: 1200px;
    height: 771px;
    overflow: hidden;
    background: var(--page);
  }
  .billboard {
    position: absolute;
    left: 139px;
    top: 201px;
    width: 921px;
    height: 368px;
    overflow: hidden;
    font-family: "Barlow Condensed", "Arial Narrow", sans-serif;
  }
  .forest-photo {
    position: absolute;
    inset: 0;
    background:
      radial-gradient(ellipse 90px 220px at 460px 170px, rgba(140,120,70,0.55), transparent 70%),
      radial-gradient(ellipse 200px 160px at 420px 80px, rgba(70,80,40,0.5), transparent 75%),
      linear-gradient(90deg, var(--forest-deep) 0%, var(--forest-mid) 45%, var(--forest-light) 52%, var(--forest-mid) 62%, var(--forest-deep) 100%);
  }
  .brand {
    position: absolute;
    left: 0;
    width: 548px;
    top: 0;
    height: 368px;
  }
  .brand-ring {
    position: absolute;
    left: 164px;
    top: 27px;
    width: 200px;
    height: 200px;
    border: 4px solid var(--white);
    border-radius: 50%;
    box-sizing: border-box;
  }
  .brand-name {
    position: absolute;
    left: 0;
    width: 548px;
    top: 236px;
    text-align: center;
    font-weight: 700;
    font-size: 58px;
    line-height: 58px;
    color: var(--name-gray);
    letter-spacing: -0.3px;
    white-space: nowrap;
  }
  .phone-row {
    position: absolute;
    left: 54px;
    width: 439px;
    top: 302px;
    display: flex;
    align-items: center;
    gap: 10px;
  }
  .phone-rule {
    flex: 1;
    height: 5px;
    background: var(--white);
    border: 1px solid var(--ink);
  }
  .phone-number {
    font-weight: 700;
    font-size: 44px;
    line-height: 44px;
    color: var(--white);
    letter-spacing: 1px;
    white-space: nowrap;
  }
  .services-panel {
    position: absolute;
    inset: 0;
  }
  .services {
    position: absolute;
    left: 574px;
    top: 22px;
    margin: 0;
    padding: 0;
    list-style: none;
  }
  .services li {
    position: relative;
    padding-left: 24px;
    font-weight: 700;
    font-size: 38px;
    line-height: 51.2px;
    color: var(--ink);
    letter-spacing: 0.6px;
    white-space: nowrap;
  }
  .services li::before {
    content: "";
    position: absolute;
    left: 0;
    top: 21px;
    width: 11px;
    height: 11px;
    border-radius: 50%;
    background: var(--ink);
  }
</style>
</head>
<body>
  <div class="billboard">
    <div class="forest-photo" role="img" aria-label="Dark forest of tall trees with a beam of sunlight in the center"></div>

    <svg class="services-panel" width="921" height="368" viewBox="0 0 921 368" aria-hidden="true">
      <polygon points="549,0 898,0 898,318 789,368 664,368 549,318" fill="var(--panel-edge)"/>
      <polygon points="549,0 898,0 898,308 776,368 677,368 549,308" fill="var(--panel)"/>
    </svg>

    <div class="brand">
      <div class="brand-ring"></div>
      <div class="brand-name">HOLLIS TREE SERVICE</div>
      <div class="phone-row">
        <span class="phone-rule"></span>
        <span class="phone-number">555-014-2368</span>
        <span class="phone-rule"></span>
      </div>
    </div>

    <ul class="services">
      <li>TREE REMOVAL</li>
      <li>TREE TRIMMING</li>
      <li>LAND DEVELOPMENT</li>
      <li>STUMP GRINDING</li>
      <li>STORM RESPONSE</li>
      <li>INSURED FREE BIDS</li>
    </ul>
  </div>
</body>
</html>
```